MAREK DOLVANE FOR CONGRESS DISTRICT 32

I need to create a campaign flyer for my congress campaign. I am running for congress in District 32 of Texas as a republican. I am a former Olympic athlete, world champion fencer, Army veteran, Counterintelligence officer (I catch spies).
I want just my first name MAREK in big letters at the top. I want it to say MAREK and below it Republican for Congress.
www.marekforcongress.example

Industry/Entity Type

Political

Colors
EB3D1F
EC4F4E
F09395
F8D3D4
FCEDEE

Requirements
Nice to have
• Would love a catchy title for the Flyer like "Spy Catcher", "Olympic Athlete" "World Champion Fencer" running for Congress in your District!

```html
<!DOCTYPE html>
<html lang="en">
<head>
<meta charset="utf-8">
<title>Marek Dolvane for Congress – Flyer</title>
<link href="https://fonts.googleapis.com/css2?family=Montserrat:wght@400;700;800&display=swap" rel="stylesheet">
<style>
  :root {
    --backdrop: #7a7a7a;
    --flyer-bg: #141518;
    --flyer-bg-soft: #1c1d21;
    --white: #ffffff;
    --campaign-red: #c8232c;
    --logo-red: #d32f2f;
    --logo-navy: #1f2f6b;
    --photo-dark: #2a2b2f;
    --photo-mid: #55565b;
    --sky-top: #7fb0e0;
    --sky-bottom: #c9b79a;
  }
  * { margin: 0; padding: 0; box-sizing: border-box; }
  html, body {
    width: 1199px;
    height: 1200px;
    overflow: hidden;
    background: var(--backdrop);
    font-family: "Montserrat", Arial, sans-serif;
  }
  .flyer {
    position: absolute;
    left: 215px;
    top: 56px;
    width: 768px;
    height: 1087px;
    background: linear-gradient(160deg, var(--flyer-bg-soft) 0%, var(--flyer-bg) 60%);
    overflow: hidden;
    color: var(--white);
  }
  .candidate-photo {
    position: absolute;
    z-index: 1;
    left: 335px;
    top: 94px;
    width: 433px;
    height: 550px;
    border-bottom-left-radius: 60px;
    background:
      linear-gradient(90deg, rgba(178,34,52,0.55) 0%, rgba(60,59,110,0.35) 22%, rgba(0,0,0,0) 34%),
      radial-gradient(ellipse at 60% 55%, var(--photo-mid) 0%, var(--photo-dark) 70%);
  }
  .campaign-logo {
    position: absolute;
    z-index: 2;
    left: 0;
    top: 54px;
    width: 400px;
    height: 174px;
    background: var(--white);
    display: flex;
    flex-direction: column;
    justify-content: center;
    padding-left: 26px;
  }
  .campaign-logo__row {
    display: flex;
    align-items: center;
    gap: 12px;
  }
  .campaign-logo__name {
    color: var(--logo-red);
    font-weight: 800;
    font-size: 33px;
    letter-spacing: 0.3px;
    line-height: 1;
    white-space: nowrap;
  }
  .campaign-logo__square {
    width: 22px;
    height: 22px;
    background: var(--logo-navy);
    flex: none;
  }
  .campaign-logo__sub {
    margin-top: 6px;
    color: var(--logo-navy);
    font-weight: 700;
    font-size: 17px;
    line-height: 1;
    text-transform: uppercase;
    white-space: nowrap;
  }
  .headline {
    position: absolute;
    z-index: 2;
    left: 65px;
    top: 300px;
    font-weight: 700;
    text-transform: uppercase;
    line-height: 1.02;
  }
  .headline__main {
    display: block;
    font-size: 35px;
  }
  .headline__sub {
    display: block;
    font-size: 22px;
    margin-top: 4px;
  }
  .tagline {
    position: absolute;
    z-index: 2;
    left: 65px;
    top: 447px;
    font-size: 21px;
    line-height: 1.3;
    font-weight: 400;
  }
  .district {
    position: absolute;
    z-index: 2;
    left: 65px;
    top: 556px;
    font-size: 25px;
    line-height: 1.3;
    font-weight: 400;
  }
  .platform {
    position: absolute;
    left: 65px;
    top: 696px;
    list-style: none;
    font-size: 21px;
    line-height: 28px;
    font-weight: 400;
  }
  .platform li {
    display: flex;
  }
  .platform li::before {
    content: "-";
    width: 35px;
    flex: none;
  }
  .capitol-image {
    position: absolute;
    left: 422px;
    top: 791px;
    width: 281px;
    height: 265px;
    background: linear-gradient(180deg, var(--sky-top) 0%, var(--sky-bottom) 100%);
  }
  .website-bar {
    position: absolute;
    left: 0;
    top: 955px;
    width: 412px;
    height: 44px;
    background: var(--campaign-red);
    display: flex;
    align-items: center;
    padding-left: 65px;
    font-size: 20px;
    font-weight: 400;
    white-space: nowrap;
  }
</style>
</head>
<body>
  <main class="flyer">
    <div class="candidate-photo" role="img" aria-label="Portrait of the candidate in a white shirt standing before an American flag"></div>

    <div class="campaign-logo">
      <div class="campaign-logo__row">
        <span class="campaign-logo__name">MAREK DOLVANE</span>
        <span class="campaign-logo__square"></span>
      </div>
      <span class="campaign-logo__sub">Republican for Congress</span>
    </div>

    <h1 class="headline">
      <span class="headline__main">Spy Catcher</span>
      <span class="headline__main">Olympic Athlete</span>
      <span class="headline__sub">World Champion Fencer</span>
    </h1>

    <p class="tagline">running for Congress<br>in your District!</p>

    <p class="district">District 32 of Texas<br>as a republican</p>

    <ul class="platform">
      <li>Stop the devaluation of the dollar.</li>
      <li>Secure the border and protect our citizens.</li>
      <li>Protect constitutional rights.</li>
      <li>Honor and Support Veterans.</li>
    </ul>

    <div class="capitol-image" role="img" aria-label="Texas state outline filled with the Capitol dome and flags"></div>

    <div class="website-bar">www.marekforcongress.example</div>
  </main>
</body>
</html>
```